Word & Power Point Templates

Microsoft Word Template: Header/Top should include my logo. Footer/Bottom should look like the bottom of the front of my business card (the orange and blue).

Microsoft Power Point Template: I want it to have a very similar look and feel to the front of my business card. Please include the logo.

```html
<!DOCTYPE html>
<html lang="en">
<head>
<meta charset="utf-8">
<title>Letterhead Template</title>
<link rel="stylesheet" href="https://fonts.googleapis.com/css2?family=Open+Sans:wght@400;600;700&display=swap">
<style>
  :root {
    --backdrop: #e9edf2;
    --paper: #ffffff;
    --brand-blue: #7ea3cc;
    --brand-blue-deep: #6c93c0;
    --brand-orange: #f9c48a;
    --title-blue: #5f8fc2;
    --page-shadow: rgba(30, 45, 70, 0.28);
  }
  * { margin: 0; padding: 0; box-sizing: border-box; }
  html, body {
    width: 1200px;
    height: 867px;
    overflow: hidden;
    background: var(--backdrop);
    font-family: "Open Sans", Arial, sans-serif;
  }
  .canvas {
    position: relative;
    width: 1200px;
    height: 867px;
  }
  .letterhead {
    position: absolute;
    left: 291px;
    top: 33px;
    width: 618px;
    height: 800px;
    background: var(--paper);
    box-shadow: 0 3px 14px var(--page-shadow);
    overflow: hidden;
  }
  .brand {
    position: absolute;
    left: 38px;
    top: 44px;
    width: 140px;
  }
  .brand-row {
    display: flex;
    align-items: center;
    gap: 7px;
  }
  .brand-dot {
    width: 14px;
    height: 14px;
    border-radius: 50%;
    background: var(--brand-blue);
    flex: none;
  }
  .brand-name {
    font-weight: 700;
    font-size: 15px;
    line-height: 1.1;
    letter-spacing: 0.5px;
    color: var(--brand-blue-deep);
    text-transform: uppercase;
  }
  .brand-tagline {
    margin-top: 5px;
    font-size: 5.5px;
    letter-spacing: 0.4px;
    color: var(--brand-orange);
    text-transform: uppercase;
    font-weight: 600;
  }
  .template-title {
    position: absolute;
    left: 238px;
    top: 106px;
    font-size: 11px;
    color: var(--title-blue);
  }
  .footer-band {
    position: absolute;
    left: 0;
    bottom: 0;
    width: 618px;
    height: 86px;
    display: block;
  }
  .band-blue { fill: var(--brand-blue); }
  .band-orange { fill: var(--brand-orange); }
</style>
</head>
<body>
<main class="canvas">
  <section class="letterhead">
    <header class="brand">
      <div class="brand-row">
        <span class="brand-dot"></span>
        <span class="brand-name">Marlowe Consulting</span>
      </div>
      <p class="brand-tagline">Shaping smart paths ahead</p>
    </header>
    <p class="template-title">Template Title</p>
    <svg class="footer-band" viewBox="0 0 618 86" preserveAspectRatio="none" aria-hidden="true">
      <path class="band-blue" d="M0 18 C150 44 380 42 618 0 L618 86 L0 86 Z"/>
      <path class="band-orange" d="M0 24 C170 50 400 50 618 26 L618 86 L0 86 Z"/>
    </svg>
  </section>
</main>
</body>
</html>
```